Holiday Rental Company Flyer Design (DL not A5)

Note from PixelFolk Administration: The category sizing selected is A5, however the project requires DL sized artwork. Please refer to the DL template link below while the 'Special Requirements' are updated accordingly.

Project Brief:
We need a double sided DL flyer designed for an up market Holiday Rental Company that portrays a personalised approach to property management. These are to be used for letter box drops to homes we're specifically targeting so the design should be modern, complimentary colour palette, uncluttered & visually appealing.

Please Download the DL Template from Quillmark here: http://www.quillmark.com.au/qm/ns/propath/UploadResources.aspx?selectedTab=0?pfid=BFB&pf_id=BFB&xnav=easypath-upload-image#Templates

Target Market(s)

Wealthy Home Owners

Industry/Entity Type

It Company

Font styles to use
Other font styles liked:
• Avant Garde Extra Light & Demi

Colors
33b8a4

Requirements
Must have
• DL Flyer sizes (210mm width x 99mm width, plus 3mm bleed)
• Front: Logo, Main Image & Grab
• Back: Contact Details & Brief Description of our business
• Images: Ideally the main image should be the house with the pool but alternatively a lifestyle images could also be used.
Nice to have
• A creative designer!
Should not have
• Clutter & busy designs

```html
<!DOCTYPE html>
<html lang="en">
<head>
<meta charset="utf-8">
<title>Harbourline Stays – DL Flyer</title>
<link rel="stylesheet" href="https://fonts.googleapis.com/css2?family=PT+Sans+Narrow:wght@400;700&display=swap">
<style>
  :root {
    --teal: #33b8a4;
    --teal-light: #5cc7b6;
    --ink: #111111;
    --black: #000000;
    --grey: #646464;
    --white: #ffffff;
    --band: rgba(232, 232, 245, 0.88);
    --condensed: "PT Sans Narrow", "Arial Narrow", sans-serif;
  }
  * { box-sizing: border-box; margin: 0; padding: 0; }
  html, body { width: 1200px; height: 1000px; overflow: hidden; background: var(--white); }
  body { position: relative; font-family: var(--condensed); color: var(--ink); }

  /* Front side */
  .front {
    position: absolute; left: 305px; top: 50px; width: 603px; height: 429px; overflow: hidden;
  }
  .front__image {
    position: absolute; inset: 0;
    background:
      linear-gradient(180deg, rgba(0,0,0,0) 70%, #2f8fd6 88%, #5ab6ee 100%),
      linear-gradient(90deg, #6b5634 0%, #c59d5e 22%, #2a2530 40%, #2a2a6a 58%, #3a2f8f 78%, #8d86d8 100%);
  }
  .front__grab {
    position: absolute; left: 0; right: 0; top: 349px; height: 60px;
    background: var(--band);
    display: flex; align-items: center; justify-content: center;
    font-size: 27px; font-weight: 400; white-space: nowrap; color: var(--ink);
  }

  /* Back side */
  .back { position: absolute; left: 300px; top: 515px; width: 605px; height: 428px; }
  .back__strip { position: absolute; left: 0; top: 0; width: 605px; height: 81px; display: flex; }
  .back__strip div { flex: 1; }
  .strip-bath { background: linear-gradient(135deg, #d9d9d6, #9a9b98); }
  .strip-sea { background: linear-gradient(180deg, #b9c7d3, #6f8aa0); }
  .strip-flowers { background: linear-gradient(135deg, #5d5750, #b06b3a 60%, #c9462f); }
  .strip-bedroom { background: linear-gradient(135deg, #d8a66a, #e8d25a 50%, #c9435e); }
  .strip-swim { background: linear-gradient(135deg, #3fc6d2, #0fa7c0); }
  .back__rule {
    position: absolute; left: 0; top: 81px; width: 605px; height: 12px;
    background: var(--black); border-bottom: 2px solid var(--teal);
  }

  .brand {
    position: absolute; left: 21px; top: 60px; width: 200px; height: 141px;
    background: var(--teal);
    box-shadow: 3px 4px 6px rgba(0,0,0,0.45);
    display: flex; flex-direction: column; align-items: center; justify-content: center; gap: 12px;
  }
  .brand__name {
    font-size: 21px; font-weight: 400; letter-spacing: 2.5px; line-height: 1.1;
    color: var(--white); text-align: center; text-transform: uppercase;
  }
  .brand__dot { width: 12px; height: 12px; border-radius: 50%; background: var(--white); opacity: 0.85; }

  .intro { position: absolute; left: 265px; top: 122px; width: 320px; }
  .intro__title { font-size: 26px; font-weight: 400; text-align: center; white-space: nowrap; }
  .intro__text {
    margin-top: 12px; font-size: 12.5px; line-height: 17px; white-space: nowrap;
  }

  .service { position: absolute; left: 0; top: 220px; width: 605px; text-align: center; }
  .service__title { font-size: 19.5px; font-weight: 400; line-height: 29px; white-space: nowrap; }
  .service__list {
    list-style: none; margin: 11px 0 0 167px; text-align: left; font-size: 11.5px; line-height: 17px;
    white-space: nowrap;
  }
  .service__list li { display: flex; align-items: center; gap: 7px; }
  .service__list li::before {
    content: ""; width: 9px; height: 9px; background: var(--teal-light); flex: none;
  }

  .contact { position: absolute; left: 0; top: 347px; width: 605px; height: 81px; display: flex; }
  .contact__prompt {
    width: 386px; background: var(--grey); color: var(--white);
    font-size: 14px; line-height: 22px; padding: 19px 0 0 25px;
    text-transform: uppercase; white-space: nowrap;
  }
  .contact__details {
    flex: 1; background: var(--black); color: var(--white); list-style: none;
    font-size: 10.5px; line-height: 16.5px; padding: 9px 0 0 42px; white-space: nowrap;
  }
  .contact__details li { display: flex; align-items: center; gap: 8px; }
  .contact__details svg { width: 9px; height: 9px; fill: var(--teal); flex: none; }
</style>
</head>
<body>

<section class="front">
  <div class="front__image" role="img" aria-label="Evening photograph of a modern luxury home with lit interiors beside a long blue swimming pool and water feature"></div>
  <h1 class="front__grab">HOLIDAY RENTAL MANAGEMENT WITH A DIFFERENCE</h1>
</section>

<section class="back">
  <div class="back__strip">
    <div class="strip-bath" role="img" aria-label="Bathroom basin with white flowers"></div>
    <div class="strip-sea" role="img" aria-label="Small boat on a calm bay"></div>
    <div class="strip-flowers" role="img" aria-label="Living room with orange flowers"></div>
    <div class="strip-bedroom" role="img" aria-label="Bedroom with bright patterned cushions"></div>
    <div class="strip-swim" role="img" aria-label="Swimmers in clear turquoise water"></div>
  </div>
  <div class="back__rule"></div>

  <div class="brand">
    <div class="brand__name">Harbourline<br>Stays</div>
    <span class="brand__dot"></span>
  </div>

  <div class="intro">
    <h2 class="intro__title">WHAT WE DO DIFFERENTLY!</h2>
    <p class="intro__text">Rather than relying upon a key safe or a central pick-up destination,<br>a ‘Harbourline Stays’ staff member will greet guests upon arrival.</p>
  </div>

  <div class="service">
    <h2 class="service__title">OUR ‘MEET &amp; GREET’ SERVICE PROVIDES HOME OWNERS WITH AN<br>INCREASED LEVEL OF SECURITY AND ALSO ALLOWS US TO:</h2>
    <ul class="service__list">
      <li>Prepare the home for their arrival (lights, heaters, music etc.)</li>
      <li>Establish a rapport &amp; help facilitate future bookings</li>
      <li>Reiterate their responsibilities to ensure the return of their bond</li>
    </ul>
  </div>

  <div class="contact">
    <p class="contact__prompt">If you’d like to know what your property could achieve or<br>require additional information, please contact us on:</p>
    <ul class="contact__details">
      <li><svg viewBox="0 0 10 10"><path d="M2 0h2l1 3-1.5 1a6 6 0 0 0 2.5 2.5L7 5l3 1v2c0 1-1 2-2 2C4 10 0 6 0 2c0-1 1-2 2-2z"/></svg>(03)5550 1294</li>
      <li><svg viewBox="0 0 10 10"><path d="M0 2h10v6H0z"/></svg>stay@harbourlinestays.com.au</li>
      <li><svg viewBox="0 0 10 10"><path d="M0 3.5a7 7 0 0 1 10 0l-1 1a5.6 5.6 0 0 0-8 0zM2 5.5a4.2 4.2 0 0 1 6 0l-1 1a2.8 2.8 0 0 0-4 0zM5 7a1.2 1.2 0 1 1 0 2.4A1.2 1.2 0 0 1 5 7z"/></svg>harbourlinestays.com.au</li>
      <li><svg viewBox="0 0 10 10"><path d="M5 0a3.5 3.5 0 0 1 3.5 3.5C8.5 6 5 10 5 10S1.5 6 1.5 3.5A3.5 3.5 0 0 1 5 0zm0 2.2a1.3 1.3 0 1 0 0 2.6 1.3 1.3 0 0 0 0-2.6z"/></svg>PO Box 12, Seaview Victoria 3999</li>
    </ul>
  </div>
</section>

</body>
</html>
```